Looking for a professional, clean and crisp business card

I am in the underground utilities industry and am just looking for a really impressive business card. I would like our card to be white with our symbol crisp and clear with it protruding. I also have a business partner that will require his name and info on the card once the design is set. I would like to have our website info on the card which is;
http://granitetrenchco.example/

Contact Information for Business Card

Website, contact name, number and email

```html
<!DOCTYPE html>
<html lang="en">
<head>
<meta charset="utf-8">
<title>Granite Trench Co – Business Card</title>
<link rel="stylesheet" href="https://fonts.googleapis.com/css2?family=Arimo:wght@400;700&display=swap">
<style>
  :root {
    --backdrop: #e8e8e8;
    --card-black: #141414;
    --card-white: #ffffff;
    --ink: #222222;
    --ink-soft: #4a4a4a;
    --brand-blue: #3a5fb0;
    --accent-red: #e41e26;
    --mark-white: #ffffff;
  }
  * { box-sizing: border-box; margin: 0; padding: 0; }
  html, body {
    width: 1200px; height: 900px; overflow: hidden;
    background: var(--backdrop);
    font-family: "Arimo", Arial, sans-serif;
  }
  .canvas { position: relative; width: 1200px; height: 900px; }

  .card {
    position: absolute; width: 600px; height: 343px;
    box-shadow: 0 6px 18px rgba(0,0,0,0.12);
  }

  /* Front */
  .card-front { left: 80px; top: 70px; background: var(--card-black); }
  .brand-front {
    position: absolute; inset: 0;
    display: flex; align-items: center; justify-content: center; gap: 14px;
  }
  .brand-front .brand-dot {
    width: 30px; height: 30px; border-radius: 50%; background: var(--brand-blue);
  }
  .brand-front .brand-name {
    color: var(--mark-white); font-weight: 700; font-size: 38px; letter-spacing: 0.5px;
  }

  /* Back */
  .card-back { left: 520px; top: 487px; background: var(--card-white); }
  .brand-back {
    position: absolute; right: 40px; top: 52px;
    display: flex; align-items: center; gap: 10px;
  }
  .brand-back .brand-dot {
    width: 20px; height: 20px; border-radius: 50%; background: var(--brand-blue);
  }
  .brand-back .brand-name {
    color: var(--ink); font-weight: 700; font-size: 22px;
  }
  .rule {
    position: absolute; left: 215px; right: 40px; top: 176px;
    height: 2px; background: var(--accent-red);
  }
  .red-tab {
    position: absolute; left: 28px; top: 160px; width: 18px; height: 50px;
    background: var(--accent-red);
  }
  .person { position: absolute; left: 62px; top: 150px; }
  .person-name {
    color: var(--brand-blue); font-weight: 700; font-size: 28px; line-height: 1;
  }
  .person-title {
    margin-top: 8px; color: var(--ink-soft); font-size: 17px;
  }
  .address {
    position: absolute; right: 40px; top: 192px; text-align: right;
    color: var(--ink); font-size: 15px; line-height: 1.3;
  }
  .contacts {
    position: absolute; left: 78px; top: 232px; list-style: none;
  }
  .contacts li {
    display: flex; align-items: center; gap: 8px;
    color: var(--ink); font-size: 16px; line-height: 22px;
  }
  .contacts svg { width: 13px; height: 13px; fill: var(--brand-blue); flex: none; }
</style>
</head>
<body>
<main class="canvas">

  <section class="card card-front" aria-label="Card front">
    <div class="brand-front">
      <span class="brand-dot"></span>
      <span class="brand-name">Granite Trench Co</span>
    </div>
  </section>

  <section class="card card-back" aria-label="Card back">
    <div class="brand-back">
      <span class="brand-dot"></span>
      <span class="brand-name">Granite Trench Co</span>
    </div>

    <div class="rule"></div>
    <div class="red-tab"></div>

    <div class="person">
      <div class="person-name">Dorian Vale</div>
      <div class="person-title">Owner/CEO</div>
    </div>

    <address class="address" style="font-style:normal">
      1480 W Cedar Avenue<br>
      Harlow County<br>
      Name 7702
    </address>

    <ul class="contacts">
      <li>
        <svg viewBox="0 0 16 16" aria-hidden="true"><path d="M3.6 1.5l2.3 2.6-1.3 1.6c.9 2 2.4 3.6 4.4 4.6l1.6-1.3 2.6 2.3-1.6 2.4C6.8 13.4 2.6 9.2 1.3 3.4z"/></svg>
        555-014-2738
      </li>
      <li>
        <svg viewBox="0 0 16 16" aria-hidden="true"><path d="M4.5 1h7a1 1 0 0 1 1 1v12a1 1 0 0 1-1 1h-7a1 1 0 0 1-1-1V2a1 1 0 0 1 1-1zm.5 2v9h6V3zm3 10a.8.8 0 1 0 0 1.6.8.8 0 0 0 0-1.6z"/></svg>
        555-019-6640
      </li>
      <li>
        <svg viewBox="0 0 16 16" aria-hidden="true"><path d="M1 3h14v10H1zm1.5 1.3V12h11V4.3L8 8.5z M2.8 4l5.2 4 5.2-4z"/></svg>
        info@granitetrenchco.example
      </li>
      <li>
        <svg viewBox="0 0 16 16" aria-hidden="true"><path d="M8 1a7 7 0 1 0 0 14A7 7 0 0 0 8 1zm0 1.5c.8 0 1.7 1.6 2 4H6c.3-2.4 1.2-4 2-4zM2.6 7.5h2a12 12 0 0 1 .4-3.9 5.5 5.5 0 0 0-2.4 3.9zm8.8 0h2A5.5 5.5 0 0 0 11 3.6c.3 1.1.4 2.5.4 3.9zM6 9h4c-.2 2.6-1.1 4.5-2 4.5S6.2 11.6 6 9z"/></svg>
        www.granitetrenchco.example
      </li>
    </ul>
  </section>

</main>
</body>
</html>
```